Business Card Design Project

We need a Business Card for an Mechanical Engineering firm in Singapore. The design should be Modern & Technical looking, yet eye catching.

Our company deals in Cutting Tools & Machine Accessories for the Manufacturing Industries such as Oil & Gas, Aero Space, etc... For more information on our Company, you can either email me or view our website www.valtrion.com.sg.

We are trying to revamp our image to give our consumers a fresh new perspective to our company, so we welcome all ideas.

Industry/Entity Type

Business

Requirements
Must have
• Must incorporate New Company Logo into the card as shown in Uploaded file.

```html
<!DOCTYPE html>
<html lang="en">
<head>
<meta charset="utf-8">
<title>Valtrion Tools – Business Card</title>
<link rel="stylesheet" href="https://fonts.googleapis.com/css2?family=Roboto:wght@400;700&display=swap">
<style>
  :root {
    --page-bg: #e6e4e1;
    --card-light: #ffffff;
    --card-light-shade: #ececec;
    --card-dark: #151515;
    --card-dark-edge: #2a2a2a;
    --magenta: #b8185e;
    --ink: #444444;
    --ink-soft: #666666;
    --paper-text: #e8e8e8;
  }
  * { box-sizing: border-box; margin: 0; padding: 0; }
  html, body {
    width: 1200px; height: 900px; overflow: hidden;
    background: var(--page-bg);
    font-family: "Roboto", Arial, sans-serif;
  }
  .canvas {
    position: relative; width: 1200px; height: 900px;
  }
  .card {
    position: absolute;
    width: 560px; height: 320px;
    border-radius: 16px;
    box-shadow: 0 10px 28px rgba(0,0,0,0.18);
    overflow: hidden;
  }
  .card--front {
    left: 110px; top: 110px;
    background: linear-gradient(180deg, var(--card-light) 0%, var(--card-light) 55%, var(--card-light-shade) 100%);
  }
  .card--back {
    left: 530px; top: 470px;
    background: radial-gradient(ellipse at 50% 45%, var(--card-dark-edge) 0%, var(--card-dark) 70%);
  }
  .brand-mark {
    display: flex; align-items: center; gap: 10px;
    font-weight: 700; color: var(--magenta);
    text-transform: uppercase; letter-spacing: 1px;
    white-space: nowrap;
  }
  .brand-mark__dot {
    width: 26px; height: 26px; border-radius: 50%;
    background: var(--magenta); flex: none;
  }
  .card--front .brand-mark {
    position: absolute; left: 40px; top: 158px; font-size: 21px;
  }
  .contact {
    position: absolute; left: 340px; top: 44px;
    color: var(--ink); font-size: 12.5px; line-height: 1.45;
  }
  .contact__name {
    color: var(--magenta); font-weight: 700; font-size: 20px; line-height: 1.1;
  }
  .contact__role { color: var(--ink-soft); font-size: 13px; margin-bottom: 22px; }
  .contact__company { font-weight: 700; }
  .contact__address { margin-bottom: 16px; }
  .contact__label { color: var(--magenta); font-weight: 700; margin-right: 4px; }
  .contact__web {
    margin-top: 14px; color: var(--magenta); font-weight: 700; font-size: 13px;
  }
  .card--back .brand-mark {
    position: absolute; left: 0; right: 0; top: 128px;
    justify-content: center; font-size: 32px;
  }
  .card--back .brand-mark__dot { width: 30px; height: 30px; }
  .back-web {
    position: absolute; left: 0; right: 0; top: 196px;
    text-align: center; color: var(--paper-text);
    font-size: 14px; letter-spacing: 2px;
  }
</style>
</head>
<body>
<main class="canvas">
  <section class="card card--front" aria-label="Business card front">
    <div class="brand-mark">
      <span class="brand-mark__dot"></span>
      <span>Valtrion Tools</span>
    </div>
    <div class="contact">
      <p class="contact__name">Mira Tanvell</p>
      <p class="contact__role">Customer Care</p>
      <p class="contact__company">Valtrion Tools Pte Ltd.</p>
      <p class="contact__address">27 Kestrel Crescent #03-12,<br>Harbourline Works Hub,<br>Singapore 139420</p>
      <p><span class="contact__label">[o]</span>65-6210 4437</p>
      <p><span class="contact__label">[f]</span>65-6210 4438</p>
      <p><span class="contact__label">[m]</span>info@valtrion.com.sg</p>
      <p class="contact__web">www.valtrion.com.sg</p>
    </div>
  </section>

  <section class="card card--back" aria-label="Business card back">
    <div class="brand-mark">
      <span class="brand-mark__dot"></span>
      <span>Valtrion Tools</span>
    </div>
    <p class="back-web">www.valtrion.com.sg</p>
  </section>
</main>
</body>
</html>
```